Stationery for London Estate Agents (Real Estate)

We are a modern and professional Estate Agency (Realtors) working with high quality properties in London.
We wish to redesign our stationary using our branding displayed on the front of our offices and require a digital version of this logo to be produced (photograph attached). Slight 'tweaking' of this branding is acceptable.
Updates
1st July 2010 Thank you all those designers who have uploaded submissions. Business Card - Details Side: Business Card - Logo Side: Outline of London Skyline Examples of the london skyline are available at http://www.pixorabank.example/searchkwy_london-skyline-silhouette Please be advised that we are looking for an outline, not a 'filled in' silhouette. Letterhead Please feel free to ask us any questions. Bertrand
I have been able to further refine our design requirements based on your submissions.
We like Blue Kettle' business card submission that has not been eliminated and have the following design clarifications;
a) Please use an email icon (e.g an envelope).
b) Please make the email as equally prominent as the telephone and fax
c) We very much like Fernwicky's 'mini window icon' - please display the website URL under such a mini window icon at the bottom right of the card.
We are very happy with the colouring, fonts and proportions used by Blue Kettle.
We invite designers to try adding an outline of the London Skyline to the left of the large window icon on the business card and in a suitablie position on the Letterhead (e.g at the top left of the letterhead).
We have the following design clarifiications to our Letterhead requirements;
A) We would like the main logo to be on the top right side of the letterhead.
B) We do NOT want the large window icon to be on the left of the logo or the bottom of the letterhead. We are happy having the large window icon to the right or underneath the TK brand.
C) Please use icons for tel, fax and email (e.g. envelope icon for e-mail address)
D) We like two coloured red borders, one at the top and bottom of the letterhead but are happy for variations in shape and size.
E) We currently prefer our address and contact details at the bottom of the letterhead.
F) We like Fernwicky's 'mini window icon' and would prefer this to be used to display the website URL at the bottom right of the letterhead.
G) Please be advised that the letterhead does NOT need additional space for the Company Name as per Blue Kettle' submission - the TK brand is sufficient.
Target Market(s)
Owners of high quality property in London.
Industry/Entity Type
Real Estate
Requirements
Must have
- Business Cards: We would like a 'vertical' style business card with our branding on one side and our staff's details on the other;
- Our website is www.tolkane.example and we are flexible where that should be on the card and letterhead.
- Stationery details are available in a file attached to this project.
Nice to have
- It would be great to have a horizontal version of the digital logo for placement on property portals (150x60)
Should not have
- Logo should not deviate significantly from the branding on our offices (shop front) - photograph attached.

```html
<!DOCTYPE html>
<html lang="en">
<head>
<meta charset="utf-8">
<title>Tolkane Residential — Business Card</title>
<link rel="stylesheet" href="https://fonts.googleapis.com/css2?family=PT+Sans:wght@400;700&display=swap">
<style>
  :root {
    --backdrop: #ece8e2;
    --card-red: #a8183f;
    --card-red-dark: #931236;
    --accent-yellow: #f3cf4b;
    --text-white: #ffffff;
    --rule-white: rgba(255,255,255,0.85);
  }
  * { box-sizing: border-box; margin: 0; padding: 0; }
  html, body {
    width: 1200px; height: 900px; overflow: hidden;
    background: var(--backdrop);
    font-family: "PT Sans", Arial, sans-serif;
  }
  .stationery {
    position: relative; width: 1200px; height: 900px;
  }
  .card {
    position: absolute; top: 140px;
    width: 400px; height: 620px;
    background: var(--card-red);
    border-radius: 4px;
    box-shadow: 0 14px 30px rgba(60,20,30,0.18);
    color: var(--text-white);
  }
  .card--brand { left: 160px; }
  .card--details { left: 640px; }

  /* Brand side */
  .brand-name {
    position: absolute; left: 46px; top: 70px;
    font-size: 40px; font-weight: 400; line-height: 1.05;
    color: var(--text-white); letter-spacing: 0.5px;
  }
  .brand-name span { display: block; }
  .brand-rule {
    position: absolute; left: 46px; top: 172px; width: 250px; height: 3px;
    background: var(--accent-yellow);
  }
  .brand-services {
    position: absolute; left: 46px; top: 188px;
    font-size: 19px; font-weight: 700; color: var(--text-white);
  }
  .brand-square {
    position: absolute; right: 56px; bottom: 70px;
    width: 130px; height: 130px; background: var(--accent-yellow);
  }

  /* Details side */
  .person-name {
    position: absolute; left: 40px; top: 50px;
    font-size: 32px; font-weight: 700;
  }
  .name-rule {
    position: absolute; left: 40px; top: 98px; width: 160px; height: 2px;
    background: var(--rule-white);
  }
  .contact-line {
    position: absolute; left: 40px;
    display: flex; align-items: center; gap: 12px;
    font-size: 20px; font-weight: 700; letter-spacing: 0.3px;
  }
  .contact-line svg { width: 22px; height: 22px; fill: var(--text-white); flex: none; }
  .contact-line--mobile { top: 112px; }
  .contact-line--phone { top: 322px; }
  .contact-line--fax { top: 366px; }
  .contact-line--email { top: 410px; }
  .contact-rule {
    position: absolute; left: 40px; width: 200px; height: 2px;
    background: var(--accent-yellow);
  }
  .contact-rule--one { top: 356px; }
  .contact-rule--two { top: 400px; }
  .office-address {
    position: absolute; left: 40px; bottom: 62px;
    font-size: 15px; font-weight: 700; line-height: 1.45;
    color: var(--accent-yellow); font-style: normal;
  }
  .web-link {
    position: absolute; right: 34px; bottom: 62px;
    display: flex; flex-direction: column; align-items: flex-end; gap: 8px;
    font-size: 14px; font-weight: 700; color: var(--accent-yellow);
  }
  .web-link .mini-square {
    width: 30px; height: 30px; background: var(--accent-yellow); margin-right: 18px;
  }
</style>
</head>
<body>
<main class="stationery">

  <section class="card card--brand" aria-label="Business card, brand side">
    <h1 class="brand-name"><span>TOLKANE</span><span>residential</span></h1>
    <div class="brand-rule"></div>
    <p class="brand-services">Sales | Lettings | Management</p>
    <div class="brand-square"></div>
  </section>

  <section class="card card--details" aria-label="Business card, details side">
    <h2 class="person-name">Bertrand Hale</h2>
    <div class="name-rule"></div>

    <p class="contact-line contact-line--mobile">
      <svg viewBox="0 0 24 24" aria-hidden="true"><path d="M8 2h8a2 2 0 0 1 2 2v16a2 2 0 0 1-2 2H8a2 2 0 0 1-2-2V4a2 2 0 0 1 2-2zm0 3v12h8V5zm4 13.5a1 1 0 1 0 0 2 1 1 0 0 0 0-2z"/></svg>
      07700 900 745
    </p>

    <p class="contact-line contact-line--phone">
      <svg viewBox="0 0 24 24" aria-hidden="true"><path d="M6.6 10.8a15.1 15.1 0 0 0 6.6 6.6l2.2-2.2a1 1 0 0 1 1-.25 11.4 11.4 0 0 0 3.6.57 1 1 0 0 1 1 1V20a1 1 0 0 1-1 1A17 17 0 0 1 3 4a1 1 0 0 1 1-1h3.5a1 1 0 0 1 1 1c0 1.25.2 2.45.57 3.57a1 1 0 0 1-.25 1z"/></svg>
      020 7946 0400
    </p>
    <div class="contact-rule contact-rule--one"></div>

    <p class="contact-line contact-line--fax">
      <svg viewBox="0 0 24 24" aria-hidden="true"><path d="M7 3h10v5H7zM4 9h16a2 2 0 0 1 2 2v6h-4v4H6v-4H2v-6a2 2 0 0 1 2-2zm4 6v4h8v-4z"/></svg>
      020 7946 0522
    </p>
    <div class="contact-rule contact-rule--two"></div>

    <p class="contact-line contact-line--email">
      <svg viewBox="0 0 24 24" aria-hidden="true"><path d="M3 5h18a1 1 0 0 1 1 1v12a1 1 0 0 1-1 1H3a1 1 0 0 1-1-1V6a1 1 0 0 1 1-1zm1 2.3V17h16V7.3l-8 5.2zM5.6 7 12 11.2 18.4 7z"/></svg>
      bertrand@tolkane.example
    </p>

    <address class="office-address">48 Elmfield Road,<br>Hampstead,<br>London NW3 9QX</address>

    <p class="web-link"><span class="mini-square"></span>www.tolkane.example</p>
  </section>

</main>
</body>
</html>
```